Facial Tissue Brand Logo and Design

We would like you to design a Logo for the Facial Tissue Brand "Velora" along with the box design. The pack should indicate the pack size (150 x 2 ply). Also our company logo should be present (attached) along with a barcode. The box size dimensions should be 210mm (L) x 110mm (W) x 70mm (H). We are open to all kinds of nice designs which are attractive but not overdone. Happy designing!

UPDATE:
We appreciate the designs so far... but would also love to see more options in a simple and elegent design style that would look good on a table... please see attached below links for reference purpose:

www.pixmarrow.com/image-photo/cleaning-wipes-isolated-on-white-480215736

www.pixmarrow.com/image-photo/cleaning-wipes-isolated-on-white-692048153

www.pixmarrow.com/image-photo/delicate-female-hands-pulling-tissue-out-2875013649

Happy desgining!

We appreciate the designs so far.. but would like to to see some more options.

```html
<!DOCTYPE html>
<html lang="en">
<head>
<meta charset="utf-8">
<title>Velora Soft Face Tissues – Box Colourways</title>
<link href="https://fonts.googleapis.com/css2?family=Great+Vibes&family=Kaushan+Script&family=Montserrat:wght@500&display=swap" rel="stylesheet">
<style>
  :root {
    --stage: #ececec;
    --white: #ffffff;
    --company-blue: #2a6db5;
    --caption-grey: #9aa3ad;

    --orange-left-a: #a8417a;
    --orange-left-b: #4a1838;
    --orange-right-a: #f39a2a;
    --orange-right-b: #ee5529;

    --pink-left-a: #4fb0f0;
    --pink-left-b: #1b67a8;
    --pink-right-a: #d9338c;
    --pink-right-b: #ff4fae;
    --pink-band: #ff7cc4;

    --green-left-a: #a6e05c;
    --green-left-b: #3f9a3a;
    --green-right-a: #4fa541;
    --green-right-b: #dcf383;
    --green-band: #d6f28a;
    --green-ink: #2f7d2f;
  }
  * { box-sizing: border-box; margin: 0; padding: 0; }
  html, body { width: 1200px; height: 912px; overflow: hidden; }
  body {
    background: radial-gradient(circle at 30% 20%, #fafafa, var(--stage));
    position: relative;
    font-family: "Montserrat", sans-serif;
  }
  .shared-defs { position: absolute; width: 0; height: 0; }

  .box {
    position: absolute;
    width: 420px;
    display: flex;
    flex-direction: column;
    border-radius: 4px;
    overflow: hidden;
    box-shadow: 0 18px 40px rgba(0,0,0,0.18);
  }
  .box--orange { left: 60px; top: 60px; }
  .box--pink { left: 660px; top: 230px; }
  .box--green { left: 120px; top: 480px; }

  .box__top, .box__front { position: relative; width: 420px; overflow: hidden; }
  .box__top { height: 220px; }
  .box__front { height: 140px; }
  .box__front::after {
    content: ""; position: absolute; inset: 0;
    background: linear-gradient(to bottom, rgba(0,0,0,0.10), rgba(0,0,0,0.02));
    pointer-events: none;
  }
  .box__art { position: absolute; inset: 0; width: 100%; height: 100%; }

  .company {
    position: absolute; left: 18px; top: 14px;
    display: flex; align-items: center; gap: 7px;
  }
  .company__mark { width: 15px; height: 15px; background: var(--company-blue); }
  .company__name { font-size: 11px; font-weight: 500; color: var(--company-blue); letter-spacing: 0.4px; }
  .company__region {
    position: absolute; left: 18px; top: 34px;
    font-size: 4px; letter-spacing: 3.5px; color: var(--caption-grey);
  }

  .badges { position: absolute; right: 50px; top: 12px; display: flex; gap: 10px; }
  .badge {
    width: 40px; height: 30px; border: 1.3px solid var(--white); border-radius: 50%;
    display: flex; flex-direction: column; align-items: center; justify-content: center;
    color: var(--white); line-height: 1;
  }
  .badge__big { font-size: 11px; font-weight: 500; }
  .badge__small { font-size: 5px; font-weight: 500; margin-top: 1px; }
  .box--green .badge { border-color: var(--green-ink); color: var(--green-ink); }

  .brand {
    position: absolute; left: 200px; top: 50px;
    font-family: "Great Vibes", cursive; font-weight: 400; font-size: 66px; line-height: 1;
    color: var(--white);
  }
  .tagline {
    position: absolute; left: 186px; top: 132px;
    font-family: "Kaushan Script", cursive; font-size: 17px; line-height: 1.05;
    color: var(--white);
  }
  .tagline span { display: block; padding-left: 12px; }

  .front-lockup { position: absolute; left: 150px; top: 32px; color: var(--white); }
  .front-lockup__tagline {
    position: absolute; left: 24px; top: 0; white-space: nowrap;
    font-family: "Kaushan Script", cursive; font-size: 9px; line-height: 1;
  }
  .front-lockup__brand {
    position: absolute; left: 0; top: 4px; white-space: nowrap;
    font-family: "Great Vibes", cursive; font-size: 48px; line-height: 1;
  }
</style>
</head>
<body>

<svg class="shared-defs" aria-hidden="true">
  <defs>
    <linearGradient id="orangeRight" x1="0" y1="0" x2="1" y2="0">
      <stop offset="0" style="stop-color:var(--orange-right-a)"/>
      <stop offset="1" style="stop-color:var(--orange-right-b)"/>
    </linearGradient>
    <linearGradient id="orangeLeft" x1="0" y1="0" x2="1" y2="0">
      <stop offset="0" style="stop-color:var(--orange-left-a)"/>
      <stop offset="1" style="stop-color:var(--orange-left-b)"/>
    </linearGradient>
    <linearGradient id="pinkRight" x1="0" y1="1" x2="1" y2="0">
      <stop offset="0" style="stop-color:var(--pink-right-a)"/>
      <stop offset="1" style="stop-color:var(--pink-right-b)"/>
    </linearGradient>
    <linearGradient id="pinkLeft" x1="0" y1="0" x2="1" y2="0">
      <stop offset="0" style="stop-color:var(--pink-left-a)"/>
      <stop offset="1" style="stop-color:var(--pink-left-b)"/>
    </linearGradient>
    <linearGradient id="greenRight" x1="0" y1="1" x2="1" y2="0">
      <stop offset="0" style="stop-color:var(--green-right-a)"/>
      <stop offset="1" style="stop-color:var(--green-right-b)"/>
    </linearGradient>
    <linearGradient id="greenLeft" x1="0" y1="0" x2="1" y2="0">
      <stop offset="0" style="stop-color:var(--green-left-a)"/>
      <stop offset="1" style="stop-color:var(--green-left-b)"/>
    </linearGradient>
    <radialGradient id="featherSoft" cx="0.5" cy="0.5" r="0.5">
      <stop offset="0" stop-color="#ffffff" stop-opacity="0.95"/>
      <stop offset="1" stop-color="#ffffff" stop-opacity="0.15"/>
    </radialGradient>
  </defs>
</svg>

<!-- Orange / plum colourway -->
<article class="box box--orange">
  <section class="box__top">
    <svg class="box__art" viewBox="0 0 420 220" preserveAspectRatio="none">
      <rect width="420" height="220" fill="url(#orangeRight)"/>
      <path d="M0 0 H235 C195 70 180 155 205 220 H0 Z" fill="url(#orangeLeft)"/>
      <path d="M0 0 H225 C225 23 195 33 171 39 C140 48 117 72 78 75 C47 78 17 90 0 103 Z" fill="var(--white)"/>
      <g role="img" aria-label="Soft white feathers drifting across the left side">
        <ellipse cx="165" cy="64" rx="26" ry="8" fill="url(#featherSoft)"/>
        <ellipse cx="118" cy="110" rx="62" ry="11" fill="url(#featherSoft)"/>
        <ellipse cx="85" cy="146" rx="78" ry="12" fill="url(#featherSoft)"/>
      </g>
      <g role="img" aria-label="Large white feather at lower right">
        <ellipse cx="345" cy="170" rx="56" ry="17" fill="url(#featherSoft)"/>
      </g>
    </svg>
    <div class="company"><span class="company__mark"></span><span class="company__name">Norvane Trading</span></div>
    <div class="company__region">UNITED ARAB EMIRATES</div>
    <div class="badges">
      <div class="badge"><span class="badge__big">150</span><span class="badge__small">TISSUES</span></div>
      <div class="badge"><span class="badge__small">WHITE</span><span class="badge__small">2 PLY</span></div>
    </div>
    <h1 class="brand">Velora</h1>
    <p class="tagline">Soft Face<span>Tissues</span></p>
  </section>
  <section class="box__front">
    <svg class="box__art" viewBox="0 0 420 140" preserveAspectRatio="none">
      <rect width="420" height="140" fill="url(#orangeRight)"/>
      <path d="M0 0 H205 C150 40 150 100 170 140 H0 Z" fill="url(#orangeLeft)"/>
      <g role="img" aria-label="Small white feathers scattered at right">
        <ellipse cx="305" cy="40" rx="34" ry="8" fill="url(#featherSoft)"/>
        <ellipse cx="380" cy="52" rx="24" ry="7" fill="url(#featherSoft)"/>
        <ellipse cx="320" cy="98" rx="30" ry="7" fill="url(#featherSoft)"/>
        <ellipse cx="385" cy="112" rx="28" ry="7" fill="url(#featherSoft)"/>
      </g>
    </svg>
    <div class="front-lockup">
      <span class="front-lockup__tagline">Soft Face Tissues</span>
      <span class="front-lockup__brand">Velora</span>
    </div>
  </section>
</article>

<!-- Pink / blue colourway -->
<article class="box box--pink">
  <section class="box__top">
    <svg class="box__art" viewBox="0 0 420 220" preserveAspectRatio="none">
      <rect width="420" height="220" fill="url(#pinkRight)"/>
      <path d="M0 0 H250 C195 62 170 155 93 220 H0 Z" fill="url(#pinkLeft)"/>
      <path d="M250 0 C195 62 170 155 93 220" fill="none" stroke="var(--pink-band)" stroke-width="5"/>
      <path d="M0 0 H225 C225 23 195 33 171 39 C140 48 117 72 78 75 C47 78 17 90 0 103 Z" fill="var(--white)"/>
      <g role="img" aria-label="Soft white feathers drifting across the left side">
        <ellipse cx="165" cy="64" rx="26" ry="8" fill="url(#featherSoft)"/>
        <ellipse cx="125" cy="112" rx="62" ry="11" fill="url(#featherSoft)"/>
        <ellipse cx="80" cy="148" rx="74" ry="12" fill="url(#featherSoft)"/>
      </g>
      <g role="img" aria-label="Large white feather at lower right">
        <ellipse cx="345" cy="170" rx="56" ry="17" fill="url(#featherSoft)"/>
      </g>
    </svg>
    <div class="company"><span class="company__mark"></span><span class="company__name">Norvane Trading</span></div>
    <div class="company__region">UNITED ARAB EMIRATES</div>
    <div class="badges">
      <div class="badge"><span class="badge__big">150</span><span class="badge__small">TISSUES</span></div>
      <div class="badge"><span class="badge__small">WHITE</span><span class="badge__small">2 PLY</span></div>
    </div>
    <h2 class="brand">Velora</h2>
    <p class="tagline">Soft Face<span>Tissues</span></p>
  </section>
  <section class="box__front">
    <svg class="box__art" viewBox="0 0 420 140" preserveAspectRatio="none">
      <rect width="420" height="140" fill="url(#pinkRight)"/>
      <path d="M0 0 H170 C150 60 110 115 60 140 H0 Z" fill="url(#pinkLeft)"/>
      <path d="M170 0 C150 60 110 115 60 140" fill="none" stroke="var(--pink-band)" stroke-width="5"/>
      <g role="img" aria-label="Small white feathers scattered at right">
        <ellipse cx="305" cy="40" rx="34" ry="8" fill="url(#featherSoft)"/>
        <ellipse cx="380" cy="52" rx="24" ry="7" fill="url(#featherSoft)"/>
        <ellipse cx="320" cy="98" rx="30" ry="7" fill="url(#featherSoft)"/>
        <ellipse cx="385" cy="112" rx="28" ry="7" fill="url(#featherSoft)"/>
      </g>
    </svg>
    <div class="front-lockup">
      <span class="front-lockup__tagline">Soft Face Tissues</span>
      <span class="front-lockup__brand">Velora</span>
    </div>
  </section>
</article>

<!-- Green / lime colourway -->
<article class="box box--green">
  <section class="box__top">
    <svg class="box__art" viewBox="0 0 420 220" preserveAspectRatio="none">
      <rect width="420" height="220" fill="url(#greenRight)"/>
      <path d="M0 0 H250 C195 62 170 155 93 220 H0 Z" fill="url(#greenLeft)"/>
      <path d="M250 0 C195 62 170 155 93 220" fill="none" stroke="var(--green-band)" stroke-width="5"/>
      <path d="M0 0 H225 C225 23 195 33 171 39 C140 48 117 72 78 75 C47 78 17 90 0 103 Z" fill="var(--white)"/>
      <g role="img" aria-label="Soft white feathers drifting across the left side">
        <ellipse cx="165" cy="64" rx="26" ry="8" fill="url(#featherSoft)"/>
        <ellipse cx="125" cy="112" rx="62" ry="11" fill="url(#featherSoft)"/>
        <ellipse cx="80" cy="148" rx="74" ry="12" fill="url(#featherSoft)"/>
      </g>
      <g role="img" aria-label="Large white feather at lower right">
        <ellipse cx="345" cy="170" rx="56" ry="17" fill="url(#featherSoft)"/>
      </g>
    </svg>
    <div class="company"><span class="company__mark"></span><span class="company__name">Norvane Trading</span></div>
    <div class="company__region">UNITED ARAB EMIRATES</div>
    <div class="badges">
      <div class="badge"><span class="badge__big">150</span><span class="badge__small">TISSUES</span></div>
      <div class="badge"><span class="badge__small">WHITE</span><span class="badge__small">2 PLY</span></div>
    </div>
    <h2 class="brand">Velora</h2>
    <p class="tagline">Soft Face<span>Tissues</span></p>
  </section>
  <section class="box__front">
    <svg class="box__art" viewBox="0 0 420 140" preserveAspectRatio="none">
      <rect width="420" height="140" fill="url(#greenRight)"/>
      <path d="M0 0 H170 C150 60 110 115 60 140 H0 Z" fill="url(#greenLeft)"/>
      <path d="M170 0 C150 60 110 115 60 140" fill="none" stroke="var(--green-band)" stroke-width="5"/>
      <g role="img" aria-label="Small white feathers scattered at right">
        <ellipse cx="305" cy="40" rx="34" ry="8" fill="url(#featherSoft)"/>
        <ellipse cx="380" cy="52" rx="24" ry="7" fill="url(#featherSoft)"/>
        <ellipse cx="320" cy="98" rx="30" ry="7" fill="url(#featherSoft)"/>
        <ellipse cx="385" cy="112" rx="28" ry="7" fill="url(#featherSoft)"/>
      </g>
    </svg>
    <div class="front-lockup">
      <span class="front-lockup__tagline">Soft Face Tissues</span>
      <span class="front-lockup__brand">Velora</span>
    </div>
  </section>
</article>

</body>
</html>
```